Community Harvest Festival Poster

Seeking a poster design to advertise our community’s annual Harvest Festival. We will utilize and display printed posters as well as distribute PDFs via our weekly e-news letters. This years "theme" is, "Copper Lantern/Maple Ridge Fair, Where City and Country Meet." The vibe is a bohemian, beatnik, street scene, meets a old fashioned orchard.

Target Market(s)

NYC School Community- should appeal to an audience that ranges from kids to grandparents. Very family oriented, with wide appeal, and must be eye catching.

Other font styles liked:
• One style should be more of a "Country" font, the other should have more of a clean city vibe.

Colors
acd037
ffc214
f68e4e
eaf2ce

Requirements
Must have
• The following copy:
• Copper Lantern Maple Ridge Fair
• Where City and Country Meet
• Celebrate C&C With Great Food, Music, Entertainment, And Fun!
• Saturday, October 19th 2019
• 12:00-4:00pm
• Tickets will be available for sale at Drop off and Pick up
Nice to have
• I'm not limited, but a couple of ideas that could be cool:
• One incorporated the background of a street, i.e. pavement, which has leaves blowing over it, and perhaps an apple or two rolling onto the page.
• Another has a diagonal breakup of the image, with one side pavement and the other side rustic wood, also with leaves sweeping across.
• I've also attached images of previous festival posters that I have gravitated to for some idea of quality I'm looking for.
Should not have
• Anything inappropriate for children.

```html
<!DOCTYPE html>
<html lang="en">
<head>
<meta charset="utf-8">
<title>Copper Lantern Maple Ridge Fair</title>
<link href="https://fonts.googleapis.com/css2?family=Rye&family=Satisfy&family=Special+Elite&display=swap" rel="stylesheet">
<style>
  :root {
    --wood-light: #f1d6ab;
    --wood-mid: #e4c08c;
    --wood-dark: #d4a870;
    --ink-brown: #4b2a16;
    --plank: #4a2d1d;
    --plank-edge: #2e1a0f;
    --post: #2b1a10;
    --sign-text: #fbf3e4;
    --leaf-red: #c9361f;
    --leaf-orange: #f68e4e;
    --leaf-gold: #ffc214;
    --leaf-green: #acd037;
    --pale: #eaf2ce;
  }
  * { margin: 0; padding: 0; box-sizing: border-box; }
  html, body { width: 900px; height: 1200px; overflow: hidden; background: #ffffff; }
  .poster {
    position: relative; width: 900px; height: 1200px; overflow: hidden;
    background: linear-gradient(100deg, var(--wood-light) 0%, var(--wood-mid) 35%, var(--wood-light) 55%, var(--wood-dark) 100%);
  }
  .foliage { position: absolute; border-radius: 50%; }
  .foliage-top {
    left: -60px; top: -120px; width: 1020px; height: 330px;
    background: radial-gradient(ellipse at 50% 40%, var(--leaf-orange) 0%, var(--leaf-red) 45%, rgba(172,208,55,0.6) 65%, rgba(241,214,171,0) 72%);
  }
  .foliage-left {
    left: -110px; top: 160px; width: 230px; height: 600px;
    background: radial-gradient(ellipse at 30% 50%, var(--leaf-green) 0%, var(--leaf-orange) 40%, rgba(201,54,31,0.5) 60%, rgba(241,214,171,0) 70%);
  }
  .foliage-right {
    left: 720px; top: 360px; width: 260px; height: 360px;
    background: radial-gradient(ellipse at 55% 45%, var(--leaf-red) 0%, var(--leaf-orange) 45%, rgba(255,194,20,0.5) 60%, rgba(241,214,171,0) 70%);
  }
  .foliage-bottom-left {
    left: -120px; top: 860px; width: 340px; height: 440px;
    background: radial-gradient(ellipse at 35% 55%, var(--leaf-orange) 0%, var(--leaf-red) 45%, rgba(172,208,55,0.5) 60%, rgba(241,214,171,0) 70%);
  }
  .foliage-bottom-right {
    left: 700px; top: 920px; width: 320px; height: 380px;
    background: radial-gradient(ellipse at 55% 60%, var(--leaf-red) 0%, var(--leaf-orange) 45%, rgba(255,194,20,0.5) 60%, rgba(241,214,171,0) 70%);
  }
  .title {
    position: absolute; left: 0; top: 248px; width: 900px; text-align: center;
    font-family: "Rye", serif; font-size: 46px; line-height: 64px; color: var(--ink-brown);
    text-shadow: 2px 2px 0 rgba(255,248,235,0.8);
    letter-spacing: 1px;
  }
  .post { position: absolute; top: 420px; width: 40px; height: 520px; background: var(--post); }
  .post-left { left: 340px; }
  .post-right { left: 540px; }
  .board {
    position: absolute; left: 200px; width: 600px;
    background: linear-gradient(180deg, #5a3724, var(--plank) 60%, #3e2517);
    border: 3px solid var(--plank-edge); border-radius: 6px;
    box-shadow: 0 6px 10px rgba(0,0,0,0.35);
    color: var(--sign-text); text-align: center;
    display: flex; align-items: center; justify-content: center;
  }
  .board-tagline { top: 455px; height: 108px; font-family: "Satisfy", cursive; font-size: 40px; }
  .board-message {
    top: 614px; height: 228px; padding: 0 40px;
    font-family: "Special Elite", monospace; font-size: 34px; line-height: 48px;
  }
  .tickets { position: absolute; left: 310px; top: 890px; width: 210px; height: 112px; }
  .ticket {
    position: absolute; width: 170px; height: 72px;
    background: var(--pale); border: 2px solid var(--ink-brown); border-radius: 6px;
  }
  .ticket-back { left: 34px; top: 34px; transform: rotate(-6deg); }
  .ticket-front {
    left: 10px; top: 12px; transform: rotate(-3deg);
    display: flex; align-items: center; justify-content: center; text-align: center;
    font-family: "Special Elite", monospace; font-size: 10.5px; line-height: 13px; color: var(--ink-brown);
    padding: 0 12px;
  }
  .ticket-front::after {
    content: ""; position: absolute; inset: 5px; border: 1px dashed var(--ink-brown); border-radius: 4px;
  }
  .event-date {
    position: absolute; left: 0; top: 1098px; width: 900px; text-align: center;
    font-family: "Special Elite", monospace; color: var(--ink-brown);
  }
  .event-day { font-size: 30px; line-height: 40px; letter-spacing: 1px; }
  .event-time { font-size: 22px; line-height: 34px; }
</style>
</head>
<body>
<main class="poster">
  <div class="foliage foliage-top" role="img" aria-label="Cluster of autumn leaves, palm fronds and flowers along the top edge"></div>
  <div class="foliage foliage-left" role="img" aria-label="Green fronds and orange leaves down the left edge"></div>
  <div class="foliage foliage-right" role="img" aria-label="Red maple leaves and berries on the right edge"></div>
  <div class="foliage foliage-bottom-left" role="img" aria-label="Orange and red autumn leaves in the lower left corner"></div>
  <div class="foliage foliage-bottom-right" role="img" aria-label="Red maple leaf in the lower right corner"></div>

  <h1 class="title">COPPER LANTERN<br>MAPLE RIDGE FAIR</h1>

  <div class="post post-left"></div>
  <div class="post post-right"></div>

  <p class="board board-tagline">Where City and Country Meet</p>
  <p class="board board-message">Celebrate C&amp;C With Great Food, Music, Entertainment, And Fun!</p>

  <div class="tickets">
    <div class="ticket ticket-back"></div>
    <div class="ticket ticket-front">TICKETS WILL BE AVAILABLE FOR SALE AT DROP OFF AND PICK UP</div>
  </div>

  <div class="event-date">
    <p class="event-day">SATURDAY, OCTOBER 19TH 2019</p>
    <p class="event-time">12:00-4:00PM</p>
  </div>
</main>
</body>
</html>
```